Brantley Yard Services Flyer Design

I need a new flyer design for my business, Brantley Yard Services. I’ll be providing my old flyer and logo as references. The new flyer should feature updated wording, contact information, logos, and photos, but still keep the original “What We Do” section and include the phrase “Don’t See? Just Ask!” somewhere near the services. The flyer needs to look great in black and white for door-to-door handouts but also be eye-catching and professional enough for social media use.

The updated content should include the headline “Transforming Outdoor Spaces with Hard Work & Precision” and highlight three main service areas: Landscaping Services (project-based landscaping to clean, prepare, and transform outdoor spaces with precision), Property Cleanup (quick hauls, debris removal, or full cleanouts—no job too big or small), and Ground Preparation (pad preparation, brush removal, and fire lines—making properties safe, functional, and project-ready).

Please also include a “Why Choose Us?” section that lists: Locally owned since 2022, Reliable & affordable – no corners cut, Professional results you can trust, LICENSED AND Insured, and Quality work / on time / references / flexible / follow-up.

At the bottom, include the contact details: Call or Text Today!
www.brantleyyard.example
| sales@brantleyyard.example
| (555) 014-2793

The overall design should be clean, professional, and easy to read with a layout that clearly shows what we offer. Use visuals that represent outdoor services, landscaping, and property cleanup/prep work. I want something that feels trustworthy, family-friendly, and modern.
Use the same photo of leaf clean up from the original flyer if possible.
Our company colors are also black and white. For the most part.

```html
<!DOCTYPE html>
<html lang="en">
<head>
<meta charset="utf-8">
<title>Brantley Yard Services Flyer</title>
<link rel="stylesheet" href="https://fonts.googleapis.com/css2?family=Archivo:wdth,wght@125,900&family=Oswald:wght@600&family=Poppins:ital,wght@0,400;0,500;0,600;0,700;0,800;1,800;1,900&display=swap">
<style>
:root{
  --ink:#000;
  --paper:#fff;
  --backdrop:#8a8a8a;
  --grass:#7a9a2a;
  --leaf:#8a4a1e;
}
*{box-sizing:border-box;margin:0;padding:0}
html,body{width:921px;height:1200px;overflow:hidden}
body{background:var(--backdrop);font-family:"Poppins",sans-serif;color:var(--ink);position:relative}
.flyer{position:absolute;left:101px;top:83px;width:719px;height:1034px;background:var(--paper);overflow:hidden}
.abs{position:absolute}

.brand{left:28px;top:30px;display:flex;align-items:center;gap:10px}
.brand-mark{width:34px;height:34px;background:var(--ink)}
.brand-name{font-weight:800;font-size:20px;line-height:1.05;text-transform:uppercase;width:200px}

.headline{left:31px;top:108px;font-weight:700;line-height:1;text-transform:uppercase}
.headline span{display:block}
.headline .md{font-size:31px;margin-bottom:6px}
.headline .lg{font-size:48px;margin-bottom:6px}
.headline .mid{font-size:35px;margin-bottom:9px}

.hero-photo{left:338px;top:0;width:381px;height:408px;
  background:linear-gradient(170deg,#6d8a22 0%,var(--grass) 40%,#a0601f 70%,var(--leaf) 100%);
  border-radius:0 0 190px 190px / 0 0 220px 220px}

.band{left:0;height:48px;background:var(--ink);color:var(--paper);
  clip-path:polygon(0 0,100% 0,calc(100% - 14px) 100%,0 100%)}
.band-line{left:0;height:48px;border-bottom:2px solid var(--ink);border-right:2px solid var(--ink);
  clip-path:polygon(0 0,100% 0,calc(100% - 14px) 100%,0 100%);background:transparent}
.band-title{position:absolute;top:50%;transform:translateY(-50%);font-weight:900;font-style:italic;font-size:26px;letter-spacing:.5px;white-space:nowrap}

.card-photo{top:430px;width:210px;height:145px;border-radius:28px 28px 28px 28px}
.card{top:528px;width:165px;height:129px;background:var(--ink);color:var(--paper);border-radius:14px;text-align:center;padding:14px 10px 0}
.card h3{font-size:12.5px;font-weight:700;line-height:1.2;text-transform:uppercase}
.card hr{width:26px;border:0;border-top:1px solid var(--paper);margin:8px auto}
.card p{font-size:10px;line-height:1.2}

.ask{left:0;width:719px;top:668px;text-align:center;font-family:"Archivo",sans-serif;font-stretch:125%;font-weight:900;font-size:33px;letter-spacing:2px}

.reason{top:783px;display:flex;align-items:center;gap:10px;font-size:12.5px;font-weight:500;line-height:1.2}
.reason-icon{width:46px;height:41px;background:var(--ink);border-radius:3px;outline:1px dashed var(--ink);outline-offset:2px;display:flex;align-items:center;justify-content:center}

.col-title{font-size:15px;font-weight:600;text-transform:uppercase}
.item{display:flex;align-items:center;gap:7px;font-size:11px;font-weight:500;position:absolute;white-space:nowrap}
.item-icon{width:18px;height:18px;border:1px solid var(--ink);border-radius:4px;display:flex;align-items:center;justify-content:center;flex:none}
.item-icon svg{width:12px;height:12px}

.footer{left:316px;top:980px;width:403px;height:54px;background:var(--ink);clip-path:polygon(22px 0,100% 0,100% 100%,0 100%)}
.footer-strip{left:0;top:1018px;width:719px;height:16px;background:var(--ink)}
.cta{color:var(--paper);font-family:"Oswald",sans-serif;font-weight:600;font-size:18px;letter-spacing:.2px}
.contact{color:var(--paper);font-size:11px;display:flex;align-items:center;gap:5px}
</style>
</head>
<body>
<div class="flyer">

  <div class="brand abs"><div class="brand-mark"></div><div class="brand-name">Brantley Yard Services</div></div>

  <h1 class="headline abs">
    <span class="md">Transforming</span>
    <span class="lg">Outdoor</span>
    <span class="mid">Spaces with</span>
    <span class="mid">Hard Work &amp;</span>
    <span class="lg">Precision</span>
  </h1>

  <div class="hero-photo abs" role="img" aria-label="Photo of a rake gathering autumn leaves on a green lawn"></div>

  <div class="band-line abs" style="top:369px;width:382px"></div>
  <div class="band abs" style="top:365px;width:380px"><span class="band-title" style="left:35px">OUR SERVICE AREAS</span></div>

  <div class="card-photo abs" style="left:26px;background:linear-gradient(160deg,#4a5a3a,#6a9a3a 60%,#3e6a2a)" role="img" aria-label="Photo of a landscaper trimming a hedge"></div>
  <div class="card-photo abs" style="left:250px;background:linear-gradient(160deg,#5a6a80,#6a6050 55%,#3a4a6a)" role="img" aria-label="Photo of a trailer loaded with junk and debris"></div>
  <div class="card-photo abs" style="left:473px;background:linear-gradient(160deg,#9a8a70,#8a8a88 55%,#b8966a)" role="img" aria-label="Photo of a prepared gravel pad beside a wood fence"></div>

  <div class="card abs" style="left:49px"><h3>Landscaping<br>Services</h3><hr><p>Project-based landscaping to clean, prepare, and transform outdoor spaces with precision</p></div>
  <div class="card abs" style="left:273px"><h3>Property<br>Cleanup</h3><hr><p>Quick hauls, debris removal, or full cleanouts—no job too big or small</p></div>
  <div class="card abs" style="left:496px;padding-top:10px"><h3>Ground<br>Preparation</h3><hr style="margin:6px auto"><p>Pad preparation, brush removal, and fire lines—making properties safe, functional, and project-ready</p></div>

  <div class="ask abs">DON’T SEE? JUST ASK!</div>

  <div class="band-line abs" style="top:727px;width:306px"></div>
  <div class="band abs" style="top:723px;width:304px"><span class="band-title" style="left:26px">WHY CHOOSE US</span></div>

  <div class="reason abs" style="left:36px">
    <div class="reason-icon"><svg width="24" height="24" viewBox="0 0 24 24" fill="none" stroke="#fff" stroke-width="1.5"><circle cx="12" cy="14" r="8"/><path d="M12 2c-2 0-3 1.4-3 3 0 2 3 5 3 5s3-3 3-5c0-1.6-1-3-3-3z"/><rect x="8" y="13" width="8" height="5"/></svg></div>
    <div>Locally owned<br>since 2022</div>
  </div>
  <div class="reason abs" style="left:206px">
    <div class="reason-icon"><svg width="26" height="26" viewBox="0 0 24 24" fill="none" stroke="#fff" stroke-width="1.5"><circle cx="12" cy="12" r="10"/><circle cx="12" cy="12" r="6"/><path d="M9 12l2 2 4-4"/></svg></div>
    <div>Licensed and<br>Insured</div>
  </div>
  <div class="reason abs" style="left:376px">
    <div class="reason-icon"><svg width="26" height="26" viewBox="0 0 24 24" fill="none" stroke="#fff" stroke-width="1.5"><circle cx="13" cy="8" r="5"/><path d="M13 5.5v5M11.5 9.5h2.5a1 1 0 000-2h-2a1 1 0 010-2h2.5"/><path d="M2 17l4-2h5l3 2h5l2-2"/><path d="M6 21l3-2h8"/></svg></div>
    <div>Reliable &amp;<br>Affordable</div>
  </div>
  <div class="reason abs" style="left:547px">
    <div class="reason-icon"><svg width="26" height="26" viewBox="0 0 24 24" fill="none" stroke="#fff" stroke-width="1.5"><circle cx="12" cy="10" r="7"/><path d="M12 6l1.2 2.5 2.7.3-2 1.9.5 2.7-2.4-1.3-2.4 1.3.5-2.7-2-1.9 2.7-.3z"/><path d="M8 16l-2 6 3-1.5L11 22M16 16l2 6-3-1.5L13 22"/></svg></div>
    <div>Quality work</div>
  </div>

  <div class="band-line abs" style="top:844px;width:306px"></div>
  <div class="band abs" style="top:840px;width:304px"><span class="band-title" style="left:31px">WHAT WE DO</span></div>

  <div class="col-title abs" style="left:32px;top:886px">Remove</div>
  <div class="item" style="left:31px;top:911px"><span class="item-icon"><svg viewBox="0 0 12 12" fill="none" stroke="#000"><path d="M2 3h8M4 3V2h4v1M3 3l1 8h4l1-8"/></svg></span>Junk Removal</div>
  <div class="item" style="left:31px;top:935px"><span class="item-icon"><svg viewBox="0 0 12 12" fill="none" stroke="#000"><rect x="2" y="4" width="8" height="7"/><path d="M4 4V2h4v2"/></svg></span>Trash &amp; Waste Hauling</div>
  <div class="item" style="left:31px;top:959px"><span class="item-icon"><svg viewBox="0 0 12 12" fill="none" stroke="#000"><path d="M2 5h7l-1 3H3z"/><circle cx="4" cy="10" r="1"/><path d="M9 5l2-2"/></svg></span>Yard and Garden Cleaning</div>
  <div class="item" style="left:31px;top:984px"><span class="item-icon"><svg viewBox="0 0 12 12" fill="none" stroke="#000"><rect x="3" y="1" width="6" height="10"/><path d="M3 4h6M4 8l3 2"/></svg></span>Appliance Removal</div>

  <div class="col-title abs" style="left:230px;top:888px">Install</div>
  <div class="item" style="left:228px;top:912px"><span class="item-icon"><svg viewBox="0 0 12 12" fill="none" stroke="#000"><path d="M1 10h10M6 10V5M6 5c0-2 2-3 4-3 0 2-2 3-4 3zM6 6C6 4 4 3 2 3c0 2 2 3 4 3z"/></svg></span>Mulch</div>
  <div class="item" style="left:228px;top:936px"><span class="item-icon"><svg viewBox="0 0 12 12" fill="none" stroke="#000"><rect x="1" y="4" width="10" height="6"/><path d="M3 6h2M7 6h2M3 8h6"/></svg></span>D.G.</div>
  <div class="item" style="left:228px;top:960px"><span class="item-icon"><svg viewBox="0 0 12 12" fill="none" stroke="#000"><path d="M3 7h6l-1 4H4zM6 7V4M6 4c-1-2-3-2-3-2s0 2 3 2zM6 4c1-2 3-2 3-2s0 2-3 2z"/></svg></span>Plants</div>
  <div class="item" style="left:228px;top:985px"><span class="item-icon"><svg viewBox="0 0 12 12" fill="#000"><path d="M1 10l3-4 2 2 2-3 3 5z"/></svg></span>Rock</div>

  <div class="col-title abs" style="left:336px;top:889px">Maintenance &amp; Other</div>
  <div class="item" style="left:336px;top:917px"><span class="item-icon"><svg viewBox="0 0 12 12" fill="none" stroke="#000"><circle cx="6" cy="2.5" r="1.2"/><path d="M6 4v4l-2 3M6 8l2 3M4 6h4M9 3l-2 8"/></svg></span>Yard clean up</div>
  <div class="item" style="left:336px;top:941px;align-items:flex-start"><span class="item-icon"><svg viewBox="0 0 12 12" fill="none" stroke="#000"><path d="M2 10l2-6M5 10l1-5M9 4l1 6M8 2l3 1"/></svg></span><span style="line-height:1.2">Weed prevention<br>(pre-emergent)</span></div>
  <div class="item" style="left:476px;top:917px"><span class="item-icon"><svg viewBox="0 0 12 12" fill="none" stroke="#000"><path d="M1 6l5-4 5 4M2 8h8l-1 2H3z"/></svg></span>Roof &amp; gutter cleaning</div>
  <div class="item" style="left:476px;top:941px"><span class="item-icon"><svg viewBox="0 0 12 12" fill="none" stroke="#000"><path d="M2 11V3l1-1 1 1v8M5 11V3l1-1 1 1v8M8 11V3l1-1 1 1v8M1 5h10M1 9h10"/></svg></span>Fence &amp; deck staining</div>

  <div class="footer abs"></div>
  <div class="footer-strip abs"></div>
  <div class="cta abs" style="left:347px;top:983px">CALL OR TEXT TODAY!</div>
  <div class="cta abs" style="left:528px;top:983px;display:flex;align-items:center;gap:6px">
    <svg width="11" height="11" viewBox="0 0 12 12" fill="none" stroke="#fff" stroke-width="1.5"><path d="M2 1h3l1 3-2 1c1 2 2 3 3 3l1-2 3 1v3c-5 1-10-4-9-9z"/></svg>(555) 014-2793</div>
  <div class="contact abs" style="left:346px;top:1011px">
    <svg width="11" height="11" viewBox="0 0 12 12" fill="none" stroke="#fff"><circle cx="6" cy="6" r="5"/><path d="M1 6h10M6 1c-2 3-2 7 0 10M6 1c2 3 2 7 0 10"/></svg>www.brantleyyard.example</div>
  <div class="contact abs" style="left:529px;top:1011px">
    <svg width="11" height="9" viewBox="0 0 12 9" fill="none" stroke="#fff"><rect x=".5" y=".5" width="11" height="8"/><path d="M.5.5l5.5 4 5.5-4"/></svg>sales@brantleyyard.example</div>
</div>
</body>
</html>
```